Keelby marketing postcards (6x9)

I would like to replicate this 6x9 postcard, but update name/logo, phone number, web address, etc. I also need to create a second postcard copying this basic design, but with updated content and background pictures. Updated contact info to be used for both postcards:
Website: www.keelbyhomestay.com
Name: Mark Tessler
Email: mtessler@keelbyhomestay.com
Phone: (555) 246-8130

Requirements
Must have
• Need two 6x9 postcard designs; 1 themed for Rivenport College, 1 for Calder State. Have uploaded photos that can be used in design. RC can be used for RC postcard (only), CS can be used for CS (only), Generic can be used for either. I've tried to upload extra photos so that you can use your creativity in selecting those that work best in the design.
Nice to have
• In the "Color palette" file, it has the two color schemes -- one for Rivenport College and one for Calder State. Those respective color schemes should be heavily represented in each design. Then there are different groups of pictures labelled either "CS" or "RC", plus some labelled "Generic". The generic ones can be used in either design, the others should be used only for the design for that school.

```html
<!DOCTYPE html>
<html lang="en">
<head>
<meta charset="utf-8">
<title>Keelby Homestay – Postcards</title>
<link href="https://fonts.googleapis.com/css2?family=Bebas+Neue&family=Montserrat:wght@500;600;700&display=swap" rel="stylesheet">
<style>
  :root {
    --paper: #ffffff;
    --stamp-grey: #e6e6e6;
    --rule-grey: #d4d4d4;
    --page-bg: #ffffff;
  }
  * { box-sizing: border-box; margin: 0; padding: 0; }
  html, body { width: 800px; height: 1200px; overflow: hidden; background: var(--page-bg); }
  body { position: relative; font-family: "Montserrat", sans-serif; }

  /* Colour schemes per school */
  .postcard-set--rivenport {
    --accent: #5166f2;
    --highlight: #4fdde0;
    --ink: #15190d;
    --ink-rgb: 21,25,13;
    --on-highlight: #0d1b4a;
    --photo-top: #3f7fd6;
    --photo-mid: #3f6a22;
    --photo-low: #2f4d1a;
    --photo-focus: #b9ab94;
  }
  .postcard-set--calder {
    --accent: #8a2332;
    --highlight: #e3b94c;
    --ink: #1a1113;
    --ink-rgb: 26,17,19;
    --on-highlight: #3a0d14;
    --photo-top: #6f9fd8;
    --photo-mid: #4c6b2e;
    --photo-low: #3b3a2a;
    --photo-focus: #c9b79a;
  }

  .postcard-set { position: absolute; top: 338px; width: 374px; }
  .postcard-set--rivenport { left: 17px; }
  .postcard-set--calder { left: 409px; }

  .postcard {
    position: absolute; left: 0; width: 720px; height: 480px;
    overflow: hidden; box-shadow: 0 3px 14px rgba(0,0,0,.4);
    transform: scale(.52); transform-origin: top left;
  }
  .postcard--front { top: 0; background: var(--ink); }
  .postcard--back { top: 274px; background: var(--paper); }

  /* FRONT */
  .hero-photo {
    position: absolute; inset: 0;
    background:
      linear-gradient(90deg, var(--ink) 0%, var(--ink) 30%, rgba(var(--ink-rgb),.75) 42%, rgba(var(--ink-rgb),0) 60%),
      radial-gradient(ellipse 18% 38% at 72% 48%, var(--photo-focus) 0%, transparent 100%),
      linear-gradient(180deg, var(--photo-top) 0%, var(--photo-top) 25%, var(--photo-mid) 62%, var(--photo-low) 85%, #8c8a7a 100%);
  }
  .brand { position: absolute; left: 40px; top: 34px; display: flex; align-items: center; gap: 12px; }
  .brand__mark { width: 30px; height: 30px; background: var(--accent); }
  .brand__name {
    font-family: "Bebas Neue", sans-serif; font-size: 30px; line-height: 1;
    color: var(--highlight); letter-spacing: .5px; padding-top: 3px;
  }
  .headline {
    position: absolute; left: 37px; top: 104px;
    font-family: "Bebas Neue", sans-serif; font-weight: 400; font-size: 72px; line-height: .88;
  }
  .headline__top { display: block; color: #fff; }
  .headline__bottom { display: block; color: var(--accent); }
  .accent-rule { position: absolute; left: 40px; top: 241px; width: 52px; height: 3px; background: var(--highlight); }
  .question {
    position: absolute; left: 40px; top: 260px;
    font-weight: 700; font-size: 21px; line-height: 1.3; color: #fff; letter-spacing: .8px;
  }
  .amount {
    position: absolute; left: 41px; top: 314px;
    font-family: "Bebas Neue", sans-serif; font-size: 84px; line-height: 1; color: var(--highlight);
  }
  .blurb {
    position: absolute; left: 43px; top: 398px; width: 232px;
    border-left: 2px solid var(--accent); padding-left: 8px;
    font-size: 9.4px; font-weight: 600; line-height: 1.3; color: #fff;
  }
  .blurb strong { color: var(--highlight); font-weight: 700; }

  .web-band {
    position: absolute; display: flex; align-items: center; gap: 10px;
    background: var(--highlight); color: var(--on-highlight);
    font-family: "Bebas Neue", sans-serif; letter-spacing: .2px; white-space: nowrap;
  }
  .web-band svg { flex: none; color: var(--accent); }
  .web-band--front {
    left: 373px; right: 0; top: 400px; height: 52px;
    border-radius: 26px 0 0 26px; padding-left: 12px; font-size: 28px;
  }

  /* BACK */
  .info-grid {
    position: absolute; left: 0; top: 0; width: 372px; height: 420px;
    display: grid; grid-template-columns: 185px 187px; grid-template-rows: 210px 210px;
  }
  .info-tile { background: var(--accent); color: #fff; font-size: 14px; font-weight: 500; line-height: 1.22; }
  .info-tile--intro { padding: 40px 10px 0 27px; }
  .info-tile--intro p + p { margin-top: 16px; }
  .info-tile--contact { padding: 22px 10px 0 20px; }
  .cta-button {
    display: inline-block; margin-top: 12px; padding: 6px 16px;
    background: var(--highlight); color: var(--on-highlight);
    border-radius: 14px; font-size: 9.5px; font-weight: 700;
  }
  .contact-details { margin-top: 10px; font-size: 9px; font-weight: 600; line-height: 1.45; }
  .contact-details__name { font-weight: 700; }
  .photo-student { background: linear-gradient(160deg, #c9ccd2 0%, #7f9bc0 40%, #5b78a8 65%, #2c3038 100%); }
  .photo-campus { background: linear-gradient(180deg, #eef0f2 0%, #d9d2c3 40%, #8a6a5e 70%, #3c4a2a 100%); }
  .web-band--back { left: 0; top: 420px; width: 372px; height: 60px; padding-left: 26px; font-size: 27px; gap: 14px; }
  .stamp-box { position: absolute; left: 589px; top: 45px; width: 102px; height: 102px; background: var(--stamp-grey); }
  .address-line { position: absolute; left: 421px; width: 266px; height: 2px; background: var(--rule-grey); }
  .address-line--1 { top: 271px; }
  .address-line--2 { top: 305px; }
  .address-line--3 { top: 339px; }
</style>
</head>
<body>

<!-- Rivenport College set -->
<div class="postcard-set postcard-set--rivenport">
  <section class="postcard postcard--front">
    <div class="hero-photo" role="img" aria-label="Photo of a Rivenport College landmark building framed by green trees under a blue sky"></div>
    <div class="brand"><span class="brand__mark"></span><span class="brand__name">Keelby Homestay</span></div>
    <h1 class="headline"><span class="headline__top">RIVENPORT</span><span class="headline__bottom">FAMILIES</span></h1>
    <div class="accent-rule"></div>
    <p class="question">WHAT WOULD YOU<br>DO WITH AN EXTRA</p>
    <p class="amount">$80,000?</p>
    <p class="blurb">The professionals at Keelby Homestay<br>are passionate about helping out-of-state families establish Texas residency and qualify for in-state tuition. Saving your family more than <strong>$13,700</strong> per semester.</p>
    <div class="web-band web-band--front">
      <svg width="30" height="30" viewBox="0 0 30 30" aria-hidden="true"><g fill="none" stroke="currentColor" stroke-width="2"><circle cx="15" cy="15" r="13"/><ellipse cx="15" cy="15" rx="6" ry="13"/><line x1="2" y1="15" x2="28" y2="15"/><line x1="4" y1="8.5" x2="26" y2="8.5"/><line x1="4" y1="21.5" x2="26" y2="21.5"/><line x1="15" y1="2" x2="15" y2="28"/></g></svg>
      <span>WWW.KEELBYHOMESTAY.COM</span>
    </div>
  </section>

  <section class="postcard postcard--back">
    <div class="info-grid">
      <div class="info-tile info-tile--intro">
        <p>Let us help you save tens of thousands of dollars on tuition in Texas.</p>
        <p>Establishing Texas<br>residency through<br>a property pur-<br>chase is as easy as<br>1-2-3.</p>
      </div>
      <div class="photo-student" role="img" aria-label="Photo of a Rivenport College student with a backpack, carrying books"></div>
      <div class="photo-campus" role="img" aria-label="Photo of a Rivenport College campus landmark behind a flowering tree"></div>
      <div class="info-tile info-tile--contact">
        <p>Contact us now to learn how Keelby Homestay is ready to become your trusted partner.</p>
        <span class="cta-button">Let us help you too!</span>
        <p class="contact-details"><span class="contact-details__name">Mark Tessler</span><br>(555) 246-8130<br>mtessler@keelbyhomestay.com</p>
      </div>
    </div>
    <div class="web-band web-band--back">
      <svg width="30" height="30" viewBox="0 0 30 30" aria-hidden="true"><g fill="none" stroke="currentColor" stroke-width="2"><circle cx="15" cy="15" r="13"/><ellipse cx="15" cy="15" rx="6" ry="13"/><line x1="2" y1="15" x2="28" y2="15"/><line x1="4" y1="8.5" x2="26" y2="8.5"/><line x1="4" y1="21.5" x2="26" y2="21.5"/><line x1="15" y1="2" x2="15" y2="28"/></g></svg>
      <span>WWW.KEELBYHOMESTAY.COM</span>
    </div>
    <div class="stamp-box"></div>
    <div class="address-line address-line--1"></div>
    <div class="address-line address-line--2"></div>
    <div class="address-line address-line--3"></div>
  </section>
</div>

<!-- Calder State set -->
<div class="postcard-set postcard-set--calder">
  <section class="postcard postcard--front">
    <div class="hero-photo" role="img" aria-label="Photo of a Calder State campus building among green trees under a blue sky"></div>
    <div class="brand"><span class="brand__mark"></span><span class="brand__name">Keelby Homestay</span></div>
    <h1 class="headline"><span class="headline__top">CALDER</span><span class="headline__bottom">FAMILIES</span></h1>
    <div class="accent-rule"></div>
    <p class="question">WHAT WOULD YOU<br>DO WITH AN EXTRA</p>
    <p class="amount">$80,000?</p>
    <p class="blurb">The professionals at Keelby Homestay<br>are passionate about helping out-of-state families establish Texas residency and qualify for in-state tuition. Saving your family more than <strong>$13,700</strong> per semester.</p>
    <div class="web-band web-band--front">
      <svg width="30" height="30" viewBox="0 0 30 30" aria-hidden="true"><g fill="none" stroke="currentColor" stroke-width="2"><circle cx="15" cy="15" r="13"/><ellipse cx="15" cy="15" rx="6" ry="13"/><line x1="2" y1="15" x2="28" y2="15"/><line x1="4" y1="8.5" x2="26" y2="8.5"/><line x1="4" y1="21.5" x2="26" y2="21.5"/><line x1="15" y1="2" x2="15" y2="28"/></g></svg>
      <span>WWW.KEELBYHOMESTAY.COM</span>
    </div>
  </section>

  <section class="postcard postcard--back">
    <div class="info-grid">
      <div class="info-tile info-tile--intro">
        <p>Let us help you save tens of thousands of dollars on tuition in Texas.</p>
        <p>Establishing Texas<br>residency through<br>a property pur-<br>chase is as easy as<br>1-2-3.</p>
      </div>
      <div class="photo-student" role="img" aria-label="Photo of a Calder State student with a backpack, carrying books"></div>
      <div class="photo-campus" role="img" aria-label="Photo of the Calder State campus water tower behind a flowering tree"></div>
      <div class="info-tile info-tile--contact">
        <p>Contact us now to learn how Keelby Homestay is ready to become your trusted partner.</p>
        <span class="cta-button">Let us help you too!</span>
        <p class="contact-details"><span class="contact-details__name">Mark Tessler</span><br>(555) 246-8130<br>mtessler@keelbyhomestay.com</p>
      </div>
    </div>
    <div class="web-band web-band--back">
      <svg width="30" height="30" viewBox="0 0 30 30" aria-hidden="true"><g fill="none" stroke="currentColor" stroke-width="2"><circle cx="15" cy="15" r="13"/><ellipse cx="15" cy="15" rx="6" ry="13"/><line x1="2" y1="15" x2="28" y2="15"/><line x1="4" y1="8.5" x2="26" y2="8.5"/><line x1="4" y1="21.5" x2="26" y2="21.5"/><line x1="15" y1="2" x2="15" y2="28"/></g></svg>
      <span>WWW.KEELBYHOMESTAY.COM</span>
    </div>
    <div class="stamp-box"></div>
    <div class="address-line address-line--1"></div>
    <div class="address-line address-line--2"></div>
    <div class="address-line address-line--3"></div>
  </section>
</div>

</body>
</html>
```